Australian Real Estate Sales Consultant needs web design please.

I am a female residential real estate sales consultant for a large australian real estate franchise.
I need a web design for "wordpress" that contains an area that will accommodate my photo and details and company logo.
A large area that contains a feature property where images are on something like a slide show.
Tabs or something similar with images for Selling, Sold, Photography and News where people can look at listings but I do not want people to be able to post a comment.
Reason: Need more designers, may be forced to change to wordpress and offer more money.
Reason: Sorry for the delay, I have been concentrating on another project which I needed completed. I am now able to focus on my web design project and hope to have it all set up in the next 10 days as it is a high priority for me. Thank you for your patience and I will begin providing feedback to your designs shortly. Thanks, Marisska.
Target Market(s)
Potential sellers or purchasers of residential property
Industry/Entity Type
Residential
Requirements
Must have
- Ease of changing property photos and info
Nice to have
- Bright attractive colours

```html
<!DOCTYPE html>
<html lang="en">
<head>
<meta charset="utf-8">
<title>Harbourline Realty</title>
<link href="https://fonts.googleapis.com/css2?family=Ubuntu:wght@300;400;500&family=Arimo:wght@400;700&display=swap" rel="stylesheet">
<style>
:root{
  --header-grey:#dcdcdc;
  --page-grey:#ececec;
  --red:#ee1d10;
  --red-dark:#b80f07;
  --navy:#14147a;
  --blue-active:#1c22b4;
  --purple:#6a2fc0;
  --purple-dark:#4a1e97;
  --ink:#1f1f1f;
  --text:#2a2a2a;
  --news-date:#1a1a8c;
  --frame:#ffffff;
  --line:#cfcfcf;
}
*{margin:0;padding:0;box-sizing:border-box}
html,body{width:1200px;height:1126px;overflow:hidden}
body{position:relative;background:var(--page-grey);font-family:"Arimo",Arial,sans-serif;color:var(--text)}
.abs{position:absolute}
.site-header{left:0;top:0;width:1200px;height:142px;background:linear-gradient(#e4e4e4,#d6d6d6)}
.brand{left:175px;top:52px;display:flex;align-items:center;gap:12px}
.brand-square{width:36px;height:36px;background:var(--navy)}
.brand-name{font-family:"Ubuntu",sans-serif;font-weight:500;font-size:30px;color:var(--navy)}
.phone-badge{left:831px;top:48px;width:54px;height:54px;border-radius:50%;background:radial-gradient(circle at 40% 35%,#f4f4f4,#bcbcbc);box-shadow:0 6px 8px rgba(0,0,0,.25);display:flex;align-items:center;justify-content:center}
.phone-number{left:895px;top:57px;font-family:"Ubuntu",sans-serif;font-size:25px;color:var(--ink)}
.main-nav{left:0;top:142px;width:1200px;height:34px;background:linear-gradient(var(--red),#d8160a);border-top:2px solid var(--red-dark);border-bottom:2px solid var(--red-dark)}
.main-nav ul{list-style:none;position:absolute;left:174px;top:0;display:flex;height:30px}
.main-nav li{font-family:"Ubuntu",sans-serif;font-size:15.5px;color:#fff;padding:0 17px;line-height:30px;border-right:1px solid rgba(120,0,0,.45)}
.main-nav li.active{background:var(--blue-active);padding:0 13px}
.search-field{left:805px;top:6px;width:215px;height:18px;background:#f4f4f4;border:1px solid #999;font-size:12px;color:#888;padding-left:4px;line-height:16px}
.search-icon{left:995px;top:0}
.feature-band{left:0;top:180px;width:1200px;height:438px;background:radial-gradient(ellipse at 50% 60%,var(--purple) 0%,#5a27ad 60%,var(--purple-dark) 100%)}
.feature-frame{left:174px;top:26px;width:855px;height:387px;background:var(--frame);padding:4px;border-radius:3px;box-shadow:0 2px 10px rgba(0,0,0,.35)}
.feature-photo{width:100%;height:100%;background:linear-gradient(#8fb0dc 0%,#c9d5e6 35%,#c9b79c 55%,#8b9a5e 85%,#7f9a4c 100%)}
.slide-arrow{top:205px}
h2{font-family:"Ubuntu",sans-serif;font-weight:400;color:var(--ink)}
.who-title{left:172px;top:630px;font-size:25px}
.body-copy{font-size:11px;line-height:16px;text-align:justify}
.who-copy{left:174px;top:668px;width:402px}
.who-copy p+p{margin-top:16px}
.who-extra{left:175px;top:850px;width:580px}
.portrait-frame{left:590px;top:631px;width:172px;height:205px;background:#fff;border:1px solid var(--line);padding:3px}
.portrait{width:100%;height:100%;background:linear-gradient(#e8e8e8 0%,#d9d2cc 45%,#2a2a2a 80%,#151515 100%)}
.news-title{left:779px;top:624px;font-size:25px}
.news-item{left:779px;width:250px;height:97px}
.news-thumb{left:0;top:0;width:76px;height:76px;background:#fff;border:1px solid var(--line);padding:3px}
.news-thumb div{width:100%;height:100%}
.news-date{left:84px;top:0;font-size:11px;font-weight:700;color:var(--news-date)}
.news-text{left:84px;top:13px;width:148px;font-size:10.5px;line-height:13px;color:var(--ink)}
.read-more{left:179px;top:64px;font-size:11px;font-weight:700;color:var(--ink);text-decoration:underline}
.news-rule{left:0;top:87px;width:250px;height:1px;background:#ddd}
.proposals-title{left:173px;top:917px;font-size:25px}
.proposals-strip{left:175px;top:955px;width:585px;height:110px;background:linear-gradient(#fbfbfb,#ededed);border:1px solid #e0e0e0;border-radius:3px}
.proposal{top:13px;width:118px;height:82px;background:#fff;border:1px solid var(--line);padding:2px}
.proposal div{width:100%;height:100%}
.strip-arrow{top:38px}
.browse-title{left:812px;top:873px;font-size:25px}
.filter{left:809px;width:190px;height:21px;background:#fff;border:1px solid #c4c4c4;font-size:12px;line-height:19px;padding-left:6px;color:var(--ink)}
.filter-toggle{position:absolute;right:3px;top:3px;width:13px;height:13px;border:1px solid #777;background:#f2f2f2}
.filter-toggle::after{content:"";position:absolute;left:3px;top:4px;border:3px solid transparent;border-top:4px solid #222}
.search-button{left:909px;top:1032px;width:90px;height:30px;background:linear-gradient(#2530d0,#0e1490);border:1px solid #fff;outline:1px solid #8a8ac8;font-family:"Arimo",sans-serif;font-weight:700;font-size:16px;color:#fff;text-align:center;line-height:28px}
.site-footer{left:0;top:1092px;width:1200px;height:34px;background:linear-gradient(var(--red),#d8160a);border-top:2px solid var(--red-dark);text-align:center;font-size:11px;line-height:32px;color:#fff}
</style>
</head>
<body>
<header class="site-header abs">
  <div class="brand abs"><span class="brand-square"></span><span class="brand-name">Harbourline Realty</span></div>
  <div class="phone-badge abs">
    <svg width="26" height="22" viewBox="0 0 26 22"><path d="M2 7c0-4 22-4 22 0v2h-5V6H7v3H2z" fill="#222"/><path d="M6 10h14l3 11H3z" fill="#222"/><circle cx="13" cy="15" r="3" fill="#ccc"/></svg>
  </div>
  <div class="phone-number abs">1300 555 019</div>
</header>

<nav class="main-nav abs">
  <ul>
    <li class="active">Home</li><li>Building</li><li>Buying</li><li>Selling</li><li>Moving</li><li>About Us</li><li>Contact Us</li>
  </ul>
  <div class="search-field abs">Search....</div>
  <svg class="search-icon abs" width="26" height="28" viewBox="0 0 26 28"><circle cx="10" cy="13" r="6" fill="none" stroke="#111" stroke-width="2.5"/><path d="M14.5 17.5l6 6" stroke="#111" stroke-width="3.5" stroke-linecap="round"/></svg>
</nav>

<section class="feature-band abs">
  <svg class="slide-arrow abs" style="left:88px" width="48" height="36" viewBox="0 0 48 36"><path d="M22 2L6 18l16 16h8L14 18 30 2zM38 2L22 18l16 16h8L30 18 46 2z" fill="#fff"/></svg>
  <div class="feature-frame abs"><div class="feature-photo" role="img" aria-label="Featured property: two-storey stucco and stone family home with garage and landscaped front garden"></div></div>
  <svg class="slide-arrow abs" style="left:1060px" width="48" height="36" viewBox="0 0 48 36"><path d="M26 2l16 16-16 16h-8l16-16L18 2zM10 2l16 16-16 16H2l16-16L2 2z" fill="#fff"/></svg>
</section>

<h2 class="who-title abs">Who We Are?</h2>
<div class="who-copy body-copy abs">
  <p>Lorem Ipsum is simply dummy text of the printing and typesetting industry. Lorem Ipsum has been the industry's standard dummy text ever since the 1500s, when an unknown printer took a galley of type and scrambled it to make a type specimen book. It has survived not only five centuries, but also the leap into electronic typesetting, remaining essentially unchanged.</p>
  <p>It was popularised in the 1960s with the release of Tessarine sheets containing Lorem Ipsum passages, and more recently with desktop publishing software like Quillset Layout including versions of Lorem Ipsum It has survived not only five centuries, but also the leap into electronic typesetting.</p>
</div>
<div class="portrait-frame abs"><div class="portrait" role="img" aria-label="Portrait photo of the sales consultant"></div></div>
<p class="who-extra body-copy abs">It was popularised in the 1960s with the release of Tessarine sheets containing Lorem Ipsum passages, and more recently with desktop publishing software like Quillset Layout including versions of Lorem Ipsum It has survived not only five centuries, but also the leap into electronic typesetting</p>

<h2 class="news-title abs">News</h2>
<article class="news-item abs" style="top:664px">
  <div class="news-thumb abs"><div role="img" aria-label="Bright modern kitchen interior" style="background:linear-gradient(#f2e7c8,#c9a86a)"></div></div>
  <div class="news-date abs">04/10/2011</div>
  <div class="news-text abs">Lorem Ipsum is simply dummy text of the printing and typesetting industry.</div>
  <div class="read-more abs">Read More</div>
  <div class="news-rule abs"></div>
</article>
<article class="news-item abs" style="top:761px">
  <div class="news-thumb abs"><div role="img" aria-label="Office meeting scene" style="background:linear-gradient(#eef1f4,#b8c0c8)"></div></div>
  <div class="news-date abs">04/10/2011</div>
  <div class="news-text abs">Lorem Ipsum is simply dummy text of the printing and typesetting industry.</div>
  <div class="read-more abs">Read More</div>
</article>

<h2 class="proposals-title abs">Our Best Proposals</h2>
<div class="proposals-strip abs">
  <svg class="strip-arrow abs" style="left:6px" width="30" height="34" viewBox="0 0 30 34"><path d="M24 2L8 17l16 15" fill="none" stroke="#c8c8c8" stroke-width="3"/></svg>
  <div class="proposal abs" style="left:46px"><div role="img" aria-label="Red brick family home" style="background:linear-gradient(#9fbde0,#a55a42 60%,#5e8a3c)"></div></div>
  <div class="proposal abs" style="left:169px"><div role="img" aria-label="Brick and stone house" style="background:linear-gradient(#c6d4de,#7a5a44 55%,#4f7a3a)"></div></div>
  <div class="proposal abs" style="left:291px"><div role="img" aria-label="House under construction" style="background:linear-gradient(#7fa6d6,#e0c060 55%,#b99a4a)"></div></div>
  <div class="proposal abs" style="left:414px"><div role="img" aria-label="Stone two-storey home" style="background:linear-gradient(#b9cbe0,#8a7a68 55%,#4e6e3c)"></div></div>
  <svg class="strip-arrow abs" style="left:548px" width="30" height="34" viewBox="0 0 30 34"><path d="M6 2l16 15L6 32" fill="none" stroke="#c8c8c8" stroke-width="3"/></svg>
</div>

<h2 class="browse-title abs">Browse Listings</h2>
<div class="filter abs" style="top:919px">Price:<span class="filter-toggle"></span></div>
<div class="filter abs" style="top:946px">Bedrooms:<span class="filter-toggle"></span></div>
<div class="filter abs" style="top:972px">Apartments:<span class="filter-toggle"></span></div>
<div class="filter abs" style="top:999px">Square Feet:<span class="filter-toggle"></span></div>
<div class="search-button abs">Search</div>

<footer class="site-footer abs">Copyright © 2003-2011 Harbourline Realty. All Rights Reserved</footer>
</body>
</html>
```